Website Landing Page for Brightfall Systems

Create a custom designed website landing page for our business. Looking for a professional upscale design that incorporates our logo and logo colors into the theme. I want a standard fixed frame website, not a constant scrolling format that seems to be the trend. To start with I'm looking for more of the graphic design part, maybe a concept or theme, I don't expect to see a finished project. Not interested in generic templates or layouts.

The name of our company is Brightfall Systems and I've attached our logo below. I'd like to have the web page have the same look and feel of our logo, as well as the colors. Our company, Brightfall Systems does system design, installation, and programming, of residential and commercial Audio/Video and Automation systems. We do home theaters, lighting and building automation, video conferencing systems, security camera installations, conference rooms, projectors, distributed audio systems, and similar Technology projects. This will be a professional services/informational website. We will not sell products on this website. This website will be used to advertise our company and communicate our services to prospective customers. Having a well designed, professional and clean website is one way we want to distinguish our company from the competition.

Here are some examples of what I consider a professional well designed website
http://www.qorlamstudio.com/Work/

Last year we had our tradlo store designed (with PixelMarket) and I'm really happy with the way it turned out. You can see it at www.HolvenGearDepot.com I consider this to be a great design and looking for the same level of quality with this new website. However, do not copy or use any part of this design in this new project. This tradlo store is completely separate from our other company Brightfall Systems. I only mention this tradlo store an an example of good work.

Reason: Still going through designs.

Reason: Still working on project and have not had time to review all designs and request revisions.

Reason: Sill going through designs and requesting revisions

Reason: still going through all the submissions we received.

Target Market(s)

People interested in Audio/Video, home theaters, home automation. We do sales, system design, and programming. We typically work on larger projects with both residential and commercial customers.

Industry/Entity Type

Business

Number of Pages Required

1 page

Requirements
Must have
• Great design elements. Please use a white background. I think white goes well with our logo colors.

```html
<!DOCTYPE html>
<html lang="en">
<head>
<meta charset="utf-8">
<title>Brightfall Systems</title>
<link href="https://fonts.googleapis.com/css2?family=Roboto:wght@300;400;500;700&display=swap" rel="stylesheet">
<style>
:root{
  --blue:#1f64ad;
  --blue-dark:#0f3f78;
  --blue-deep:#0a2c58;
  --teal:#1b9ad6;
  --green:#3fa535;
  --green-dark:#1f7a1d;
  --green-light:#66c43f;
  --text:#444;
  --muted:#777;
  --line:#d8d8d8;
  --footer:#1c1c1c;
  --footer-text:#9a9a9a;
}
*{box-sizing:border-box;margin:0;padding:0}
html,body{width:814px;height:1200px;overflow:hidden;background:#fff}
body{font-family:'Roboto',Arial,sans-serif;color:var(--text);position:relative}
.abs{position:absolute}

/* top bar */
.topbar{left:0;top:0;width:814px;height:29px;border-bottom:1px solid #e6e6e6}
.topbar .welcome{left:146px;top:13px;font-size:7.5px;color:#555}
.phone-btn{left:274px;top:8px;width:92px;height:20px;background:linear-gradient(#4cb53d,#2f8a27);border:1px solid #2a7d23;color:#fff;font-size:10px;font-weight:500;display:flex;align-items:center;gap:10px;padding-left:8px}
.topbar .connect{left:542px;top:13px;font-size:7.5px;color:#555}
.sq{top:8px;width:16px;height:18px;border-radius:2px}
.sq.a{left:608px;background:#3b5b99}
.sq.b{left:630px;background:#1a6aa0}
.sq.c{left:651px;background:#d23b2e}

/* header */
.brand{left:146px;top:44px;display:flex;align-items:center;gap:10px}
.brand .ring{width:54px;height:54px;border-radius:50%;border:5px solid var(--teal)}
.brand .name{font-size:16px;font-weight:500;line-height:16px;color:var(--teal);letter-spacing:1px}
.nav{left:348px;top:60px;width:466px;height:46px;background:linear-gradient(#f4f4f4,#d9d9d9);clip-path:polygon(22px 0,100% 0,100% 100%,0 100%)}
.nav ul{list-style:none;display:flex;position:absolute;left:34px;top:20px}
.nav li{font-size:7px;color:#666;padding:0 13px;border-right:1px solid #c8c8c8}
.nav li:last-child{border-right:none}
.nav li.active{color:var(--blue);font-weight:700}

/* hero */
.hero-photo{left:0;top:109px;width:814px;height:200px;background:linear-gradient(100deg,#2b4150 0%,#7a5a33 35%,#c98d4a 55%,#8a6a45 72%,#b7a68e 100%)}
.hero-panel{left:0;top:109px;width:350px;height:200px;background:linear-gradient(160deg,rgba(40,110,180,.95),rgba(18,70,130,.95));clip-path:polygon(0 0,100% 0,80% 100%,0 100%)}
.hero h1{left:146px;top:148px;font-size:17px;font-weight:700;color:#fff;line-height:19px}
.hero p{left:146px;top:190px;width:150px;font-size:8px;line-height:11.5px;color:#fff}
.btn-read{left:146px;top:244px;width:68px;height:21px;background:linear-gradient(#fff,#d9dde3);border:1px solid #9aa9bb;color:var(--blue);font-size:7.5px;font-weight:700;display:flex;align-items:center;justify-content:center}
.caption{left:288px;top:257px;width:526px;height:29px;background:linear-gradient(90deg,rgba(20,20,20,.2),rgba(20,20,20,.75) 8%,rgba(20,20,20,.5))}
.caption .t{left:14px;top:10px;font-size:8.5px;font-weight:700;color:#fff}
.caption .d{left:242px;top:12px;font-size:6px;font-weight:700;color:#8bd44a}
.band{left:0;top:309px;width:814px;height:22px}

/* areas */
.tab{left:348px;top:360px;width:141px;height:28px;background:linear-gradient(#54b83f,#2e8d27);color:#fff;font-size:10.5px;font-weight:700;display:flex;align-items:center;justify-content:center;border-top:2px solid #7ad25a}
.rule{left:204px;top:388px;width:408px;height:1px;background:linear-gradient(90deg,transparent,#cfcfcf 20%,#cfcfcf 80%,transparent)}
.intro{left:250px;top:394px;width:314px;font-size:7px;line-height:11px;color:var(--muted);text-align:center}

.card{width:152px;height:103px}
.card::before{content:"";position:absolute;left:-4px;top:-5px;right:-5px;bottom:-6px;background:var(--green);clip-path:polygon(74% 0,100% 0,100% 100%,42% 100%)}
.card .photo{position:absolute;inset:0;border:2px solid #fff;box-shadow:0 0 2px rgba(0,0,0,.3)}
.card .label{position:absolute;left:4px;bottom:41px;font-size:9.5px;color:#fff;line-height:11px;text-transform:uppercase}
.card .label b{font-weight:700}
.card .more{position:absolute;left:-4px;top:68px;width:60px;height:15px;background:var(--blue);clip-path:polygon(0 0,88% 0,100% 50%,88% 100%,0 100%);color:#fff;font-size:6px;font-weight:700;padding:4px 0 0 8px}
.c1{left:150px;top:434px}.c2{left:331px;top:434px}.c3{left:512px;top:434px}
.c4{left:150px;top:575px}.c5{left:331px;top:575px}.c6{left:512px;top:575px}
.c1 .photo{background:linear-gradient(135deg,#3a3a3a,#6c6f6c 50%,#2a2d2f)}
.c2 .photo{background:linear-gradient(135deg,#4b3a25,#a58654 50%,#3c2e1f)}
.c3 .photo{background:linear-gradient(135deg,#1d4f86,#3b79b9 60%,#c7d3de)}
.c4 .photo{background:linear-gradient(135deg,#2b2520,#6a4a34 55%,#a36b45)}
.c5 .photo{background:linear-gradient(135deg,#4e4536,#8d7f68 55%,#4e7a3a)}
.c6 .photo{background:linear-gradient(135deg,#5a4336,#9b8d84 55%,#2e2e2e)}

/* overview */
.ov-title{left:146px;top:735px;font-size:12px;font-weight:400;color:#333;letter-spacing:.3px}
.ov-title b{font-weight:700}
.ov-rule{left:146px;top:753px;width:364px;height:3px;background:repeating-linear-gradient(90deg,#d4d4d4 0 1px,#fff 1px 2px)}
.ov-brand{left:146px;top:762px;display:flex;align-items:center;gap:6px}
.ov-brand .ring{width:34px;height:34px;border-radius:50%;border:3px solid #b5b5b5}
.ov-brand .name{font-size:9px;font-weight:500;line-height:10px;color:#aaa;letter-spacing:.5px}
.lede{left:146px;top:803px;font-size:7.5px;font-weight:700;color:var(--blue)}
.ov-text{left:146px;top:815px;width:364px;font-size:7.5px;line-height:11px;color:#555;text-align:justify}
.ov-text b{color:var(--green);font-weight:700}

.services{left:146px;top:861px;width:364px;height:114px;background:var(--blue)}
.services .inner{position:absolute;left:6px;top:6px;right:6px;bottom:6px;border:1px solid rgba(255,255,255,.35)}
.services .head{left:18px;top:45px;font-size:11px;color:#fff;line-height:13px}
.services .head b{font-weight:700}
.services ul{list-style:none;position:absolute;left:136px;top:19px}
.services li{font-size:10px;font-weight:500;color:#fff;height:12px;margin-bottom:9px;display:flex;align-items:center;gap:7px}
.services .sub{left:136px;top:81px;width:220px;font-size:7.5px;color:#dce8f6;line-height:10px}

/* contact form */
.contact{left:530px;top:737px;width:138px;height:238px;background:var(--green)}
.contact .card-in{position:absolute;left:7px;top:10px;width:124px;height:214px;background:#fff}
.contact h3{position:absolute;left:7px;top:8px;font-size:10px;font-weight:400;color:#222}
.contact h3 b{font-weight:700}
.contact .tag{position:absolute;left:7px;top:21px;font-size:6px;color:#888}
.contact .hr{position:absolute;left:0;top:30px;width:124px;height:3px;background:var(--blue-deep)}
.field{position:absolute;left:6px;width:112px;height:25px;background:#efefef;border:1px solid #d3d3d3;font-size:7px;color:#999;padding:8px 6px}
.f1{top:44px}.f2{top:77px}.f3{top:110px}.f4{top:143px;height:43px}
.submit{position:absolute;left:5px;top:198px;width:128px;height:24px;background:linear-gradient(#1c5da6,#0c3565);color:#fff;font-size:9.5px;font-weight:700;display:flex;align-items:center;justify-content:center}

/* footer */
.footer{left:0;top:1014px;width:814px;height:156px;background:var(--footer);border-top:4px solid #e6e6e6}
.f-brand{left:146px;top:1044px;display:flex;align-items:center;gap:6px}
.f-brand .ring{width:26px;height:26px;border-radius:50%;border:3px solid #444}
.f-brand .name{font-size:7px;line-height:8px;color:#4a4a4a;letter-spacing:.4px}
.map{left:146px;top:1082px;width:124px;height:62px;background:linear-gradient(135deg,#e6e2d6,#f2efe8 55%,#d9dfe6)}
.addr{left:277px;top:1082px;font-size:7px;line-height:10px;color:var(--footer-text);display:flex;gap:5px}
.f-phone{left:277px;top:1110px;font-size:10.5px;color:var(--green-light);display:flex;gap:4px;align-items:center}
.f-mail{left:277px;top:1136px;font-size:7px;color:var(--footer-text);display:flex;gap:4px;align-items:center}
.f-h{font-size:8.5px;font-weight:700;color:#fff}
.nav-h{left:422px;top:1049px}
.nav-rule{left:422px;top:1062px;width:76px;height:1px;background:#3a3a3a}
.f-links{left:422px;top:1071px;list-style:none}
.f-links li{font-size:7px;color:#8a8a8a;margin-bottom:7.5px}
.mail-h{left:525px;top:1048px}
.mail-rule{left:525px;top:1062px;width:143px;height:1px;background:#3a3a3a}
.mail-in{left:525px;top:1070px;width:142px;height:18px;background:#fff;border:2px solid #cfcfcf;font-size:7px;color:#444;padding:3px 4px}
.mail-btn{left:525px;top:1094px;width:55px;height:18px;background:linear-gradient(#4cb53d,#2f8a27);border:1px solid #8bd44a;color:#fff;font-size:7px;font-weight:700;display:flex;align-items:center;justify-content:center}
.f-connect{left:525px;top:1129px;font-size:7.5px;color:#fff}
.dot{top:1125px;width:16px;height:16px;border-radius:50%;border:1px solid #fff}
.dot.a{left:596px;background:#3b5b99}
.dot.b{left:624px;background:#1a6aa0}
.dot.c{left:652px;background:#d23b2e}

.bottom{left:0;top:1170px;width:814px;height:30px;background:#fff}
.copy{left:146px;top:1181px;font-size:7px;color:#666}
.copy span{color:var(--green)}
.legal{left:542px;top:1181px;font-size:7px;color:#666;word-spacing:2px}
</style>
</head>
<body>

<!-- top bar -->
<div class="abs topbar">
  <div class="abs welcome">Welcome to Brightfall Systems</div>
  <div class="abs phone-btn">
    <svg width="8" height="8" viewBox="0 0 24 24"><path fill="#fff" d="M6.6 10.8a15 15 0 0 0 6.6 6.6l2.2-2.2a1 1 0 0 1 1-.25 11.4 11.4 0 0 0 3.6.57 1 1 0 0 1 1 1V20a1 1 0 0 1-1 1A17 17 0 0 1 3 4a1 1 0 0 1 1-1h3.5a1 1 0 0 1 1 1c0 1.25.2 2.45.57 3.57a1 1 0 0 1-.25 1z"/></svg>
    555.014.7290
  </div>
  <div class="abs connect">Connect With Us</div>
  <div class="abs sq a" role="img" aria-label="Social profile"></div>
  <div class="abs sq b" role="img" aria-label="Social profile"></div>
  <div class="abs sq c" role="img" aria-label="Social profile"></div>
</div>

<!-- header -->
<div class="abs brand">
  <div class="ring"></div>
  <div class="name">BRIGHTFALL<br>SYSTEMS</div>
</div>
<nav class="abs nav">
  <ul>
    <li class="active">HOME</li><li>ABOUT US</li><li>SERVICES</li><li>WHY US</li><li>CONTACT US</li>
  </ul>
</nav>

<!-- hero -->
<section class="hero">
  <div class="abs hero-photo" role="img" aria-label="Evening view of a lit villa entrance with palm trees"></div>
  <div class="abs hero-panel"></div>
  <h1 class="abs">BRIGHTFALL<br>SYSTEMS</h1>
  <p class="abs">Does system design, installation, and programming, of residential and commercial Audio/Video and Automation systems.</p>
  <div class="abs btn-read">READ MORE</div>
  <div class="abs caption">
    <div class="abs t">LIGHTING AND BUILDING AUTOMATION SYSTEMS</div>
    <div class="abs d">DETAILS ▸</div>
  </div>
  <svg class="abs band" width="814" height="22" viewBox="0 0 814 22">
    <polygon points="276,0 330,0 310,22 290,22" fill="#d4d4d4"/>
    <polygon points="320,0 814,0 814,22 300,22" fill="#2f8a27"/>
    <polygon points="320,0 380,0 360,22 300,22" fill="#6cc94a"/>
  </svg>
</section>

<!-- areas we serve -->
<div class="abs tab">AREAS WE SERVE</div>
<div class="abs rule"></div>
<p class="abs intro">Lorem Ipsum is simply dummy text of the printing and typesetting industry. Lorem Ipsum has been the industry's standard dummy text ever since the 1500s</p>

<div class="abs card c1"><div class="photo" role="img" aria-label="Auditorium set up for video conferencing"></div><div class="label">Video<br><b>Conferencing</b></div><div class="more">READ MORE ▸</div></div>
<div class="abs card c2"><div class="photo" role="img" aria-label="Ornate hall with chandelier lighting"></div><div class="label">Lighting<br><b>and Building<br>Automation</b></div><div class="more">READ MORE ▸</div></div>
<div class="abs card c3"><div class="photo" role="img" aria-label="Security cameras on a wall"></div><div class="label">Security<br><b>Camera<br>Installations</b></div><div class="more">READ MORE ▸</div></div>
<div class="abs card c4"><div class="photo" role="img" aria-label="Bar counter with stools and ceiling speakers"></div><div class="label">Distributed<br><b>Audio Systems</b></div><div class="more">READ MORE ▸</div></div>
<div class="abs card c5"><div class="photo" role="img" aria-label="Living room with large wall screen"></div><div class="label">Home<br><b>Theaters</b></div><div class="more">READ MORE ▸</div></div>
<div class="abs card c6"><div class="photo" role="img" aria-label="Conference room with long table and chairs"></div><div class="label">Conference<br><b>Rooms</b></div><div class="more">READ MORE ▸</div></div>

<!-- company overview -->
<h2 class="abs ov-title">COMPANY <b>OVERVIEW</b></h2>
<div class="abs ov-rule"></div>
<div class="abs ov-brand"><div class="ring"></div><div class="name">BRIGHTFALL<br>SYSTEMS</div></div>
<p class="abs lede">Lorem Ipsum is simply dummy text of the printing and typesetting industry.</p>
<p class="abs ov-text">Lorem Ipsum has been the industry's standard dummy text ever since the 1500s, when an unknown printer took a galley of type and scrambled it to make a type specimen book. It has survived not only five centuries, but also the leap into electronic typesetting, remaining essentially unchanged. <b>MORE ▸</b></p>

<div class="abs services">
  <svg class="abs" style="left:0;top:0" width="364" height="114" viewBox="0 0 364 114">
    <polygon points="6,6 130,6 76,108 6,108" fill="#0d3a70"/>
    <line x1="128" y1="-4" x2="74" y2="116" stroke="#3fa535" stroke-width="3"/>
  </svg>
  <div class="inner"></div>
  <div class="abs head">Our<br><b>SERVICES</b></div>
  <ul>
    <li><svg width="9" height="9" viewBox="0 0 10 10"><circle cx="5" cy="5" r="4.3" fill="none" stroke="#fff"/><path d="M4 3l2 2-2 2" fill="none" stroke="#fff"/></svg>System Design</li>
    <li><svg width="9" height="9" viewBox="0 0 10 10"><circle cx="5" cy="5" r="4.3" fill="none" stroke="#fff"/><path d="M4 3l2 2-2 2" fill="none" stroke="#fff"/></svg>Installation</li>
    <li><svg width="9" height="9" viewBox="0 0 10 10"><circle cx="5" cy="5" r="4.3" fill="none" stroke="#fff"/><path d="M4 3l2 2-2 2" fill="none" stroke="#fff"/></svg>Programming</li>
  </ul>
  <div class="abs sub">Of residential and commercial Audio/Video and Automation systems.</div>
</div>

<!-- contact form -->
<div class="abs contact">
  <div class="card-in">
    <h3>CONTACT <b>US</b></h3>
    <div class="tag">Lorem Ipsum is simply dummy</div>
    <div class="hr"></div>
    <div class="field f1">Name:</div>
    <div class="field f2">Email:</div>
    <div class="field f3">Phone:</div>
    <div class="field f4">Message:</div>
  </div>
  <div class="submit">SUBMIT</div>
</div>

<!-- footer -->
<footer class="abs footer"></footer>
<div class="abs f-brand"><div class="ring"></div><div class="name">BRIGHTFALL<br>SYSTEMS</div></div>
<div class="abs map" role="img" aria-label="Street map showing the office location"></div>
<div class="abs addr">
  <svg width="7" height="9" viewBox="0 0 10 14"><path d="M5 0a5 5 0 0 0-5 5c0 4 5 9 5 9s5-5 5-9a5 5 0 0 0-5-5zm0 7a2 2 0 1 1 0-4 2 2 0 0 1 0 4z" fill="#4cb53d"/></svg>
  <div>418-2290 Varnel Street<br>Ashbourne NH 11547</div>
</div>
<div class="abs f-phone">
  <svg width="8" height="8" viewBox="0 0 24 24"><path fill="#4cb53d" d="M6.6 10.8a15 15 0 0 0 6.6 6.6l2.2-2.2a1 1 0 0 1 1-.25 11.4 11.4 0 0 0 3.6.57 1 1 0 0 1 1 1V20a1 1 0 0 1-1 1A17 17 0 0 1 3 4a1 1 0 0 1 1-1h3.5a1 1 0 0 1 1 1c0 1.25.2 2.45.57 3.57a1 1 0 0 1-.25 1z"/></svg>
  555.014.7290
</div>
<div class="abs f-mail">
  <svg width="8" height="6" viewBox="0 0 12 9"><rect x=".5" y=".5" width="11" height="8" fill="none" stroke="#4cb53d"/><path d="M.5.5 6 5l5.5-4.5" fill="none" stroke="#4cb53d"/></svg>
  hello@brightfallsystems.com
</div>

<div class="abs f-h nav-h">NAVIGATE</div>
<div class="abs nav-rule"></div>
<ul class="abs f-links"><li>Home</li><li>About Us</li><li>Services</li><li>Why Us</li><li>Contact Us</li></ul>

<div class="abs f-h mail-h">JOIN OUR MAILING LIST:</div>
<div class="abs mail-in">Email Address</div>
<div class="abs mail-btn">SUBMIT</div>
<div class="abs f-connect">Connect With Us</div>
<div class="abs dot a" role="img" aria-label="Social profile"></div>
<div class="abs dot b" role="img" aria-label="Social profile"></div>
<div class="abs dot c" role="img" aria-label="Social profile"></div>

<div class="abs bottom"></div>
<div class="abs copy">Copyright © 2017 <span>Brightfall Systems</span>. All Rights Reserved.</div>
<div class="abs legal">Sitemap &nbsp;|&nbsp; Privacy Policy &nbsp;|&nbsp; Legal</div>

</body>
</html>
```